月経前症候群(PMS)に悩む女性向けにマニュアル配布をする
オプトLPのファーストビュー画像の制作(PC+スマホ)です。

- 案件名
美容LP(PMS訴求)のファーストビュー制作

- 目的
アドレス登録

- ターゲット
PMSに苦しんでいる20〜40代女性
特にイライラ、食欲増加、むくみ

- 制作範囲
スマホ・PC版のファーストビュー(CTAボタンまで)
CTA付近に、下のオファー内容をPCと書籍のモックアップで入れる

- コピー原稿+レイアウト参考
https://notes.paperlyn-share.net/document/d/7Qx2RbWm9KfTz3LpVn8YcH4sJd6UeA1oGi0NwMkZrXt/edit?usp=sharing

- コピー原稿
イライラ・食欲増加・むくみ
何をやってもよくならないPMSが良くなるマニュアル

- 強調ポイント
PMSが良くなる←下のURL1つ目の画像の「1年で結婚したい」のイメージ
マニュアル←「あなたのための婚活セミナー」
https://hanamori-zuan.jp/25/001-3/

- デザイン参考

- メイン画像:
PMSがよくなってにこやかな女性

- カラー
暖色系

- 納品
・透過PNG
(CTAエリアの入力フォームの前後で2つに分割して書き出していただきます)
・AI or PS, XD(元データ)
暖色系 ※どこかでこの色を使って欲しいです(#542D24)
コンペでは、スマホ版だけでオッケーです。当確後、PC版含めて納品いただければと思います。
モックアップの詳細の記載がないとのコメントをいただきましたが、コピー原稿に掲載があります。
それをPC画面と書籍の2パターンでご制作ください。

よろしくお願いいたします。

クオリティが高く、素敵なデザインだったので選ばせていただきました。
すごくセンスの良いデザイナーさんだと思いました。

とても悩んだので選ぶのに時間がかかってしまい
お待たせしてすみませんでした。
この度は素敵なデザインを本当にありがとうございました。

```html
<!DOCTYPE html>
<html lang="ja">
<head>
<meta charset="UTF-8">
<title>PMSが良くなるマニュアル 無料プレゼント</title>
<link rel="stylesheet" href="https://fonts.googleapis.com/css2?family=Shippori+Mincho:wght@600;800&family=Zen+Maru+Gothic:wght@500;700&family=Noto+Sans+JP:wght@400;500;700&display=swap">
<style>
:root{
  --brown:#542D24;
  --purple:#8a3f9c;
  --circle-a:#b36ac4;
  --circle-b:#8d3aa3;
  --ribbon:#e889b4;
  --ribbon-deep:#d86b9f;
  --pink-bg:#f6b9d3;
  --pink-soft:#fde9f2;
  --top-bg:#fbf3f6;
  --highlight:#fff08a;
  --green:#34b24a;
  --green-light:#6fd66a;
  --green-shadow:#248a36;
  --white:#ffffff;
  --line:#d9cdd2;
  --placeholder:#9a9a9a;
  --cover:#fde4ec;
  --cover-edge:#c9a9b5;
  --cover-shadow:#e9d6dd;
}
*{margin:0;padding:0;box-sizing:border-box}
html,body{width:835px;height:1200px;overflow:hidden;background:var(--white)}
.canvas{position:relative;width:835px;height:1200px;overflow:hidden;font-family:"Noto Sans JP",sans-serif;color:var(--brown)}

/* hero */
.hero{position:absolute;left:0;top:0;width:835px;height:515px;background:linear-gradient(180deg,var(--white) 0%,var(--top-bg) 100%)}
.hero-photo{position:absolute;right:0;top:0;width:470px;height:515px;background:radial-gradient(ellipse at 60% 40%,#f1d8cf 0%,#e8c4bf 35%,#f4e6ea 70%,rgba(251,243,246,0) 100%)}
.symptoms{position:absolute;left:40px;top:-14px;display:flex;gap:12px}
.symptom{width:152px;height:152px;border-radius:50%;background:radial-gradient(circle at 40% 35%,var(--circle-a),var(--circle-b));display:flex;align-items:center;justify-content:center;padding-top:34px;color:var(--white);font-family:"Zen Maru Gothic",sans-serif;font-weight:700;font-size:33px;letter-spacing:1px}
.ribbon{position:absolute;left:80px;top:190px;width:480px;height:56px;background:linear-gradient(90deg,var(--ribbon-deep),var(--ribbon));display:flex;align-items:center;justify-content:center;color:var(--white);font-family:"Shippori Mincho",serif;font-weight:800;font-size:32px;letter-spacing:2px;white-space:nowrap;clip-path:polygon(0 0,100% 0,96% 50%,100% 100%,0 100%,4% 50%)}
.headline{position:absolute;left:30px;top:258px;z-index:1;font-family:"Shippori Mincho",serif;font-weight:800;color:var(--brown);line-height:1;white-space:nowrap}
.headline-main{display:block;font-size:120px;letter-spacing:-2px;transform:skewX(-8deg);transform-origin:left bottom}
.headline-main .rest{font-size:86px;letter-spacing:0}
.headline-sub{position:relative;display:inline-block;margin-top:14px;margin-left:140px;font-size:86px;color:var(--purple);letter-spacing:4px}
.headline-sub::after{content:"";position:absolute;left:-6px;right:-10px;bottom:-2px;height:22px;background:var(--highlight);z-index:-1}

/* offer */
.offer{position:absolute;left:0;top:515px;width:835px;height:685px;background:linear-gradient(180deg,var(--pink-bg) 0%,var(--pink-soft) 100%)}
.offer-card{position:absolute;left:40px;top:25px;width:755px;height:630px;background:var(--white);border-radius:6px}
.book{position:absolute;left:18px;top:15px;width:300px;height:318px;background:var(--cover);border:2px solid var(--cover-edge);box-shadow:8px 8px 0 var(--cover-shadow)}
.book-tags{display:flex;justify-content:center;gap:8px;margin-top:12px}
.book-tag{width:46px;height:46px;border-radius:50%;background:var(--circle-b);color:var(--white);font-size:9px;display:flex;align-items:center;justify-content:center;font-weight:700}
.book-title{text-align:center;margin-top:8px;font-family:"Shippori Mincho",serif;font-weight:800;line-height:1.12}
.book-title .s{display:block;font-size:13px;white-space:nowrap}
.book-title .l{display:block;font-size:32px}
.book-title .m{display:block;font-size:22px;color:var(--purple)}
.book-figure{position:absolute;left:16px;bottom:12px;width:66px;height:84px;background:linear-gradient(180deg,#f5d9cf,#e9b9c6);border-radius:8px}
.book-author{position:absolute;right:24px;bottom:20px;text-align:right;font-family:"Shippori Mincho",serif;font-weight:800;font-size:14px;line-height:1.4}
.book-author b{display:block;font-size:20px}
.present{position:absolute;left:350px;top:32px;width:390px;height:64px;background:linear-gradient(90deg,var(--ribbon-deep),var(--ribbon));color:var(--white);font-family:"Zen Maru Gothic",sans-serif;font-weight:700;font-size:36px;display:flex;align-items:center;justify-content:center;letter-spacing:2px;clip-path:polygon(0 0,100% 0,100% 100%,0 100%,5% 50%)}
.present-title{position:absolute;left:350px;top:118px;width:390px;text-align:center;font-family:"Shippori Mincho",serif;font-weight:800;line-height:1.25;border-bottom:2px solid var(--brown);padding-bottom:8px;white-space:nowrap}
.present-title .s{display:block;font-size:28px}
.present-title .l{display:block;font-size:40px}
.present-title .m{display:block;font-size:30px}
.present-author{position:absolute;left:350px;top:292px;width:390px;text-align:center;font-family:"Shippori Mincho",serif;font-weight:800;font-size:32px;letter-spacing:2px}
.email-field{position:absolute;left:56px;top:358px;width:642px;height:88px;border:2px solid var(--line);background:var(--white);display:flex;align-items:center;padding-left:28px;color:var(--placeholder);font-size:28px;letter-spacing:2px}
.cta{position:absolute;left:56px;top:466px;width:642px;height:116px;border-radius:58px;background:linear-gradient(180deg,var(--green-light),var(--green));box-shadow:0 6px 0 var(--green-shadow);display:flex;align-items:center;justify-content:center;gap:18px;color:var(--white);font-family:"Zen Maru Gothic",sans-serif;font-weight:700;font-size:44px;letter-spacing:2px;white-space:nowrap}
.cta svg{width:50px;height:50px}
</style>
</head>
<body>
<div class="canvas">
  <section class="hero">
    <div class="hero-photo" role="img" aria-label="PMSが良くなり明るく微笑む女性の写真"></div>
    <div class="symptoms">
      <div class="symptom">イライラ</div>
      <div class="symptom">食欲不振</div>
      <div class="symptom">むくみ</div>
    </div>
    <div class="ribbon">何をやってもよくならない</div>
    <h1 class="headline">
      <span class="headline-main">PMS<span class="rest">が良くなる</span></span>
      <span class="headline-sub">マニュアル</span>
    </h1>
  </section>

  <section class="offer">
    <div class="offer-card">
      <div class="book">
        <div class="book-tags">
          <span class="book-tag">イライラ</span>
          <span class="book-tag">食欲不振</span>
          <span class="book-tag">むくみ</span>
        </div>
        <div class="book-title">
          <span class="s">何をやってもよくならない</span>
          <span class="l">PMSが<br>良くなる</span>
          <span class="m">マニュアル</span>
        </div>
        <div class="book-figure" role="img" aria-label="表紙の女性イラスト"></div>
        <div class="book-author">美容家<b>花井 美咲 著</b></div>
      </div>
      <div class="present">無料プレゼント</div>
      <div class="present-title">
        <span class="s">何をやってもよくならない</span>
        <span class="l">PMSが良くなる</span>
        <span class="m">マニュアル</span>
      </div>
      <div class="present-author">花井 美咲 著</div>
      <div class="email-field">メールアドレスを入力</div>
      <div class="cta">
        <svg viewBox="0 0 50 50" aria-hidden="true"><circle cx="25" cy="25" r="22" fill="none" stroke="#fff" stroke-width="4"/><path d="M20 15 L35 25 L20 35 Z" fill="#fff"/></svg>
        <span>今すぐ無料で手に入れる</span>
      </div>
    </div>
  </section>
</div>
</body>
</html>
```